Website - TSCR

Having reviewed the designs received so far, no one design is meeting the client’s needs. The client has identified desirable elements from the designs submitted, which we want to see brought together.
Header
It is important that the logo is given space – ie is not overlayed on an image, nor with a short fade into an image. A gradual fade into the header image is acceptable.
Background
While an image background is acceptable, this should only be visible on the left and right borders, it should not be used underneath the main content area.
Main menu
The main menu should be a cohesive bar across the page – not separate buttons. Buttons that are connected together within a bar are acceptable. Menu items should be separated using a pipe ( | ), or by being framed (as long as the framing sits within a bar). Menu item should change colour to indicate the page you are on.
Left Hand Boxes
There should be consistency in colouring through these. It is acceptable to use one colour for the heading , and another for the content area. It is not acceptable for each box to have a different scheme. This applies to the right hand feature boxes as well.
Colouring
We want to keep this simple. Please use colours from the logo, feel free to add complimentary colours but keep the palette limited. If shading is used with any of the colours be careful to not move it too far from the original colour. The yellow does not look good with too much of a grey shade.
Feature Boxes
The two feature boxes on the home page (Browse Homes and Local Knowledge) need to stand out. An option is to ensure that the associated link button uses one of the brighter colours in the palette.
_____________________________________________________
Note: I have attached the newly design logo to the brief. It is important that colours from the logo are used on the design. Blue denotes water and the yellow denotes sand and sun.
I'd like to see the feel of the logo reflected in the site.
______________________________________________
Tui Shore and Coastal Retreats is rebuilding its website – www.tuishoreandcoastalretreats.co.nz.
We require the design of two pages:
• Home
• House detail page (pgs 3-5 of the attachment).
We have specified a layout for the site (attached).
The contextual information below provides the feeling the site needs to convey.
If further information is required please contact us.
CONTEXT/BACKGROUND
Tui Shore and Coastal Retreats (TSCR) has been in business now for over 11 years and is due for a facelift. We have about 40 – 60 houses available during the peak summer period – about 50% are permanent holiday homes, the balance are local family homes being rented out while they are away on holiday.
We are currently located in Ohope Beach – but with the national name have the ability and goal to expand into other areas of New Zealand – so any logo etc has to have the ability to represent other holiday destinations within NZ. Bear in mind that our primary location is Ohope at the moment.
Our key market is families going on holiday – looking for a holiday home to book (currently an Ohope Beach holiday)
Secondary market is couples or mature groups looking at having some R&R or business groups having some team building/ management meetings away from the busy office surroundings.
We manage ALL the properties so are a great source of information on what holiday home is best suited to each family and “things to do” in the area – i.e. other activities.
Our main focus is to be the best “holiday home” - accommodation provider in whatever location TSCR is representing. We want to be seen as having a good supply of great homes, providing a great service as well as being a good source of local knowledge.
We want to be seen as PROFESSIONALS in the holiday rental business (from occupants and owners).
TRUST – we want people to be able to trust us by listing their property with us (owners) and confidently booking accommodation through us (occupants).
TAGLINE SUGGESTIONS
Key motif – “TSCR, your door to a fine escape!” The “key”, of course is a double play on the house key you get. But it is also extendible to other aspect of the experience we offer. For example the phrase: “getting the key to the city” is applicable to us – we give them the key to Ohope…(or whatever location we are marketing in the future). Potentially we may consider promotional merchandise around this, eg promo key rings etc.
Some key words/phrases that our business represents are:
• ‘Our place is your place’
• Connect – connecting families to holiday homes and the area – at the moment only Ohope.
• Local – local people looking after your needs – “our place is your place – so make yourself at home!”
• Link – we are the link to a real kiwi holiday experience.
• Holiday - R&R – rest and recreation
More specific to Ohope:
• Safe Natural playground – beach, bush, fishing, outdoor activities – creating real family memories.
Website:
• Need to focus on the Local and Personal property management factors in website to differentiate us from other nationwide listing sites – contact us and we can help you find the right accommodation and save you time
• Play on the HOLIDAYMAKER experience more, including giving prominence to visitor deals, become a local etc, differentiating us from other local holiday home rental businesses.
• Real – real people, real places, real experiences.
• User friendly, informative, professional with a personal touch/feel, to encourage the holiday feeling.
Reason: We had put this project on hold pending the design of a new logo.
Having reviewed the designs received so far, no one design is meetingthe client’s needs. The client has identified desirable elements from thedesigns submitted, which we want to see brought together.
Header
It is important that the logo is given space – ie is not overlayed on animage, nor with a short fade into an image. A gradual fade into the headerimage is acceptable.
Background
While an image background is acceptable, this should only be visible onthe left and right borders, it should not be used underneath the main contentarea.
Main menu
The main menu should be a cohesive bar across the page – not separatebuttons. Buttons that are connected together within a bar are acceptable.Menu items should be separated using a pipe ( | ), or by being framed (as longas the framing sits within a bar). Menu item should change colour to indicatethe page you are on.
Left Hand Boxes
There should be consistency in colouring through these. It isacceptable to use one colour for the heading , and another for the contentarea. It is not acceptable for each box to have a different scheme. Thisapplies to the right hand feature boxes as well.
Colouring
We want to keep this simple. Please use colours from the logo,feel free to add complimentary colours but keep the palette limited. Ifshading is used with any of the colours be careful to not move it too far fromthe original colour. The yellow does not look good with too much of agrey shade.
Feature Boxes
The two feature boxes on the home page (Browse Homes and LocalKnowledge) need to stand out. An option is to ensure that the associated linkbutton uses one of the brighter colours in the palette.

```html
<!DOCTYPE html>
<html lang="en">
<head>
<meta charset="utf-8">
<title>Tui Shore and Coastal Retreats</title>
<link rel="stylesheet" href="https://fonts.googleapis.com/css2?family=Questrial&family=Arimo:wght@400;700&display=swap">
<style>
:root{
  --ocean-deep:#0b3f7e;
  --ocean:#1a74c4;
  --sky:#dcedf9;
  --cream:#fbf1d2;
  --bar-top:#7a7a7a;
  --bar-bottom:#3f3f3f;
  --panel:#f1f1f1;
  --panel-line:#c9c9c9;
  --sun:#f3c21a;
  --sun-light:#fde36a;
  --teal-top:#7fc3d6;
  --teal-bottom:#3f95ad;
  --sand:#dcd4b4;
  --ink:#1b1b1b;
  --muted:#6a6a6a;
}
*{box-sizing:border-box;margin:0;padding:0}
html,body{width:1156px;height:1200px;overflow:hidden}
body{
  position:relative;
  font-family:"Arimo",Arial,sans-serif;
  color:var(--ink);
  background:radial-gradient(ellipse at 50% 45%,var(--ocean) 0%,var(--ocean-deep) 75%,#072a57 100%);
}
.abs{position:absolute}
.page{left:108px;top:0;width:935px;height:1200px;background:var(--sky)}
.header{left:108px;top:0;width:935px;height:174px;background:linear-gradient(#ffffff,var(--cream))}
.brand{left:150px;top:50px;width:230px;display:flex;align-items:center;gap:10px;font-family:"Questrial",sans-serif;font-size:19px;line-height:23px;color:#3a3a3a}
.brand-dot{flex:none;width:26px;height:26px;border-radius:50%;background:var(--sun)}
.strip{left:402px;top:36px;width:600px;height:88px;border:2px solid #e3e3e3;border-radius:12px;overflow:hidden;display:flex;background:#fff}
.strip div{flex:1}
.strip .p1{background:linear-gradient(#7fb6df,#e9c48d)}
.strip .p2{background:linear-gradient(120deg,#d79a6e,#c0704a)}
.strip .p3{background:linear-gradient(#3d8fcf,#d7b080)}
.nav{left:144px;top:137px;width:858px;height:36px;border-radius:6px 6px 0 0;background:linear-gradient(var(--bar-top),var(--bar-bottom));display:flex;align-items:center;padding-left:15px;font-family:"Questrial",sans-serif;font-size:14px;color:#fff}
.nav span.sep{margin:0 14px;color:#ddd}
.nav .current{color:var(--sun-light)}
.shortlist{position:absolute;right:8px;top:7px;width:115px;height:22px;border-radius:4px;background:linear-gradient(var(--sun-light),var(--sun));color:#3a2a00;font-size:14px;text-align:center;line-height:22px}
.band{left:118px;top:174px;width:923px;height:297px;background:linear-gradient(90deg,#1457a0,#2a86d0 50%,#1457a0)}
.hero{left:144px;top:176px;width:858px;height:294px;border:2px solid #fff;background:linear-gradient(#9fc3d8 0%,#3f7a45 30%,#2f6b3a 60%,#2fa3b0 80%,#e8dcc0 100%)}
.box{width:200px;background:var(--panel);border:1px solid var(--panel-line);border-radius:6px 6px 0 0}
.box-head{height:36px;border-radius:6px 6px 0 0;background:linear-gradient(#8a8a8a,#3f3f3f);color:#fff;font-family:"Questrial",sans-serif;font-size:15px;line-height:38px;padding-left:9px}
.label{font-size:11px;font-weight:700;margin:0 0 2px 8px}
.select{display:inline-block;height:20px;border:1px solid #aaa;background:#fff;position:relative}
.select::after{content:"";position:absolute;right:0;top:0;width:16px;height:18px;border-left:1px solid #ccc;background:linear-gradient(#fff,#ddd)}
.field{height:20px;border:1px solid #aaa;background:#fff;font-size:11px;color:#666;padding:3px 5px}
.btn-go{height:20px;width:31px;border:1px solid #999;background:linear-gradient(#fff,#ddd);font-size:10px;font-weight:700;text-align:center;line-height:18px}
.copy{font-size:11px;line-height:13.1px;color:#222}
.help-body{text-align:center;font-size:11px;font-weight:700;line-height:21.6px;padding-top:8px}
.cta{left:352px;top:798px;width:650px;height:62px;border-radius:6px;background:linear-gradient(var(--teal-top),var(--teal-bottom));border:1px solid #a8d4e0;color:#fff;font-family:"Questrial",sans-serif;font-size:23px;line-height:26px;text-align:center;padding-top:5px}
.feature{width:316px;height:204px;border:1px solid #c8c1a3;background:var(--sand)}
.feature .photo{margin:3px;height:152px}
.feature .title{font-family:"Questrial",sans-serif;font-size:23px;text-align:center;line-height:44px}
.deal{display:flex;gap:12px;padding:8px 10px 6px 10px}
.deal .thumb{width:68px;height:56px;border:3px solid #fff;outline:1px solid #bbb}
.deal .info{font-size:10px;line-height:14px;color:var(--muted)}
.deal .info b{color:var(--ink)}
.deal .info a{color:var(--ink);text-decoration:underline}
.social{width:24px;height:24px;border-radius:4px}
.footer{font-size:11px;color:#222}
</style>
</head>
<body>
<div class="abs page"></div>
<header class="abs header"></header>
<div class="abs brand"><span class="brand-dot"></span><span>Tui Shore and<br>Coastal Retreats</span></div>
<div class="abs strip"><div class="p1" role="img" aria-label="Family walking on the beach"></div><div class="p2" role="img" aria-label="Friends taking a holiday photo"></div><div class="p3" role="img" aria-label="Family playing at the shore"></div></div>

<nav class="abs nav">
  <span class="current">Home</span><span class="sep">|</span>
  <span>Browse Home</span><span class="sep">|</span>
  <span>Packages</span><span class="sep">|</span>
  <span>local Knowledge</span><span class="sep">|</span>
  <span>About Us</span><span class="sep">|</span>
  <span>Contact Us</span><span class="sep">|</span>
  <span>List Your Home</span>
  <span class="shortlist">My Short List</span>
</nav>

<div class="abs band"></div>
<div class="abs hero" role="img" aria-label="Thatched beach pavilion and jetty below green tropical mountains"></div>

<section class="abs box" style="left:144px;top:490px;height:192px">
  <div class="box-head">Quick Search</div>
  <div style="padding-top:14px">
    <p class="label">No. Of Guests</p>
    <div style="margin-left:8px"><span class="select" style="width:91px"></span></div>
    <p class="label" style="margin-top:14px">Nightly Rate</p>
    <div style="margin-left:8px"><span class="select" style="width:82px"></span><span class="select" style="width:82px;margin-left:19px"></span></div>
    <p class="label" style="margin-top:14px">Keywords</p>
    <div style="margin-left:8px;display:flex;gap:8px"><div class="field" style="width:145px">Beach access</div><div class="btn-go">GO</div></div>
  </div>
</section>

<section class="abs box" style="left:144px;top:698px;height:176px">
  <div class="box-head">Keep In Touch</div>
  <p style="font-size:11px;font-weight:700;text-align:center;line-height:13px;margin-top:6px">Newsletter with deals &amp; Local<br>Knowledge to Your Inbox.</p>
  <div class="field" style="width:145px;margin:10px 0 0 28px">Name...</div>
  <div class="field" style="width:145px;margin:10px 0 0 28px">Emails...</div>
  <div class="btn-go" style="margin:10px 0 0 141px">GO</div>
</section>

<section class="abs box" style="left:144px;top:888px;height:191px">
  <div class="box-head">Deals</div>
  <div class="deal" style="border-bottom:1px solid #ccc;margin:0 8px;padding-left:2px">
    <div class="thumb" role="img" aria-label="White holiday house" style="background:linear-gradient(#8fb2d6,#c7c7c7 50%,#6b8a4f)"></div>
    <div class="info">Loreum Ipsum Set<br>Price : $ 500.00<br><b>Special : $ 450.00</b><br><a>View Details</a></div>
  </div>
  <div class="deal" style="margin:0 8px;padding-left:2px">
    <div class="thumb" role="img" aria-label="Bedroom interior" style="background:linear-gradient(90deg,#4e5a66,#9aa7b3)"></div>
    <div class="info">Loreum Ipsum Set<br>Price : $ 500.00<br><b>Special : $ 450.00</b><br><a>View Details</a></div>
  </div>
</section>

<div class="abs" style="left:298px;top:1085px;width:46px;height:20px;border:1px solid #aab;border-radius:3px;background:#fff;font-size:10px;text-align:center;line-height:18px;color:#3b5998">Like</div>
<div class="abs" style="left:144px;top:1109px;display:flex;gap:5px;align-items:center">
  <span class="social" style="background:#3b5998"></span>
  <span class="social" style="background:#f08a24"></span>
  <span class="social" style="background:#e0407f"></span>
  <span class="social" style="background:#4fb4e6"></span>
  <span class="social" style="background:#1f7ab8"></span>
  <span style="font-size:12px;font-weight:700;margin-left:3px">Share this</span>
</div>

<h1 class="abs" style="left:351px;top:496px;font-family:'Questrial',sans-serif;font-size:14px;font-weight:400">Welcome to Our Website</h1>
<p class="abs copy" style="left:353px;top:516px;width:460px">Lorem Ipsum is simply dummy text of the printing and typesetting industry. Lorem Ipsum has been the industry's standard dummy text ever since the 1500s, when an unknown printer took a galley of type and scrambled it to make a type specimen book. It has survived not only five centuries, but also the leap into electronic typesetting, remaining essentially unchanged. It was popularised in the 1960s with the release of Lettrex sheets containing Lorem Ipsum passages, and more recently with desktop publishing software like Folio PageSetter including versions of Lorem Ipsum.</p>
<p class="abs copy" style="left:353px;top:620px;width:470px">Lorem Ipsum is simply dummy text of the printing and typesetting industry. Lorem Ipsum has been the industry's standard dummy text ever since the 1500s, when an unknown printer took a galley of type and scrambled it to make a type specimen book. It has survived not only five centuries, but also the leap into electronic typesetting, remaining essentially unchanged. It was popularised in the 1960s with the release of Lettrex sheets containing Lorem Ipsum passages, and more recently with desktop publishing software like Folio PageSetter including versions of Lorem Ipsum.</p>
<p class="abs copy" style="left:355px;top:723px;width:646px">Lorem Ipsum is simply dummy text of the printing and typesetting industry. Lorem Ipsum has been the industry's standard dummy text ever since the 1500s, when an unknown printer took a galley of type and scrambled it to make a type specimen book. It has survived not only five centuries, but also the leap into electronic typesetting, remaining essentially unchanged. It was popularised in the 1960s with the release of Lettrex sheets containing Lorem Ipsum passages, and more recently with desktop publishing software like Folio PageSetter including versions of Lorem Ipsum.</p>

<section class="abs box" style="left:824px;top:492px;width:175px;height:159px">
  <div class="box-head" style="text-align:center;padding-left:0">Help!</div>
  <div class="help-body">Can't find what you are<br>looking for ?<br>Contact us for A<br>Personal Property Search<br>+64-27-555-0148</div>
</section>

<div class="abs cta">Just Can't find what you are looking for ? Contact Us for a<br>Personal Property Search.</div>

<article class="abs feature" style="left:357px;top:873px">
  <div class="photo" role="img" aria-label="Holiday home kitchen and dining room" style="background:linear-gradient(#3b56a8 0%,#c9c6c0 40%,#8a6a45 100%)"></div>
  <div class="title">Browse Home</div>
</article>
<article class="abs feature" style="left:686px;top:873px">
  <div class="photo" role="img" aria-label="Garden pergola beside a house" style="background:linear-gradient(#d7dde0 0%,#9a8f78 45%,#6e7b54 100%)"></div>
  <div class="title">Local Knowledge</div>
</article>

<p class="abs copy" style="left:355px;top:1088px;width:646px">Lorem Ipsum is simply dummy text of the printing and typesetting industry. Lorem Ipsum has been the industry's standard dummy text ever since the 1500s, when an unknown printer took a galley of type and scrambled it to make a type specimen book. It has survived not only five centuries, but also the leap into electronic typesetting.</p>

<footer>
  <p class="abs footer" style="left:146px;top:1163px">Copyright © 2011 tuishoreandcoastalretreats.</p>
  <p class="abs footer" style="right:157px;top:1163px">Terms &amp; Conditions &nbsp;|&nbsp; Privacy Policy &nbsp;|&nbsp; Contact Us &nbsp;|&nbsp; List Your Name</p>
</footer>
</body>
</html>
```